International Medical travel company needs professional card

We just purchased a logo through sketch nest, and now need a business card. We contract with Middle Eastern governments to bring patients who need complex medical care to the U.S. for treatment. We will upload logo. Titles, names, contact info, etc. needs to be in English on one side, Arabic on the other

Target Market(s)

Health administrators, professionals

Industry/Entity Type

Health Care

Contact Information for Business Card

logo on each side. Usual name/title/contact info

Font styles to use
Serif
Sans Serif

Colors
0255a3

Requirements
Must have
• English one side, Arabic the other

```html
<!DOCTYPE html>
<html lang="en">
<head>
<meta charset="utf-8">
<title>Arven Health – Business Card</title>
<link rel="stylesheet" href="https://fonts.googleapis.com/css2?family=Open+Sans:wght@400;600&display=swap">
<style>
  :root {
    --backdrop: #4a4a4a;
    --card: #1d1d1d;
    --brand-blue: #0255a3;
    --link-blue: #1a6cc0;
    --gold: #c9b431;
    --ink-dark: #1b2433;
    --ink-light: #e6e6e6;
  }
  * { margin: 0; padding: 0; box-sizing: border-box; }
  html, body {
    width: 1105px; height: 1200px; overflow: hidden;
    background: var(--backdrop);
    font-family: "Open Sans", Arial, sans-serif;
  }
  .business-card {
    position: absolute; left: 102px; top: 343px;
    width: 900px; height: 514px;
    background: var(--card);
    overflow: hidden;
  }
  .header-band {
    position: absolute; left: 0; top: 0;
    width: 100%; height: 148px;
    background: var(--brand-blue);
  }
  .holder-name {
    position: absolute; left: 43px; top: 40px;
    font-size: 29px; font-weight: 600; color: var(--ink-dark);
    letter-spacing: 0.5px;
  }
  .holder-title {
    position: absolute; left: 43px; top: 80px;
    font-size: 22px; color: var(--ink-dark);
  }
  .brand-square {
    position: absolute; left: 655px; top: 41px;
    width: 150px; height: 128px;
    border: 5px solid var(--gold);
  }
  .brand-name {
    position: absolute; left: 560px; width: 340px; top: 172px;
    text-align: center; color: var(--gold);
    font-weight: 400; line-height: 1;
  }
  .brand-name .primary { display: block; font-size: 62px; letter-spacing: 2px; }
  .brand-name .secondary { display: block; font-size: 21px; letter-spacing: 3px; margin-top: 6px; }
  .contact-list {
    position: absolute; left: 43px; top: 344px;
    list-style: none;
  }
  .contact-list li {
    display: flex; align-items: center;
    height: 33.5px;
    font-size: 23px; color: var(--ink-light);
  }
  .contact-list svg { width: 22px; height: 22px; margin-right: 11px; fill: var(--link-blue); }
  .address {
    position: absolute; right: 43px; top: 354px;
    text-align: right; font-style: normal;
    font-size: 23px; line-height: 31px; color: var(--ink-light);
  }
  .address .website {
    color: var(--link-blue); letter-spacing: 3px; font-size: 22px;
  }
</style>
</head>
<body>
  <section class="business-card">
    <div class="header-band"></div>
    <h1 class="holder-name">OMAR HADDAD</h1>
    <p class="holder-title">CEO/FOUNDER</p>

    <div class="brand-square" aria-hidden="true"></div>
    <p class="brand-name"><span class="primary">ARVEN</span><span class="secondary">HEALTH</span></p>

    <ul class="contact-list">
      <li><svg viewBox="0 0 24 24"><path d="M6.6 10.8a15.1 15.1 0 0 0 6.6 6.6l2.2-2.2c.3-.3.7-.4 1-.2 1.1.4 2.3.6 3.6.6.6 0 1 .4 1 1V20c0 .6-.4 1-1 1A17 17 0 0 1 3 4c0-.6.4-1 1-1h3.5c.6 0 1 .4 1 1 0 1.3.2 2.5.6 3.6.1.3 0 .7-.2 1z"/></svg>614 205 7391</li>
      <li><svg viewBox="0 0 24 24"><path d="M7 1h10a2 2 0 0 1 2 2v18a2 2 0 0 1-2 2H7a2 2 0 0 1-2-2V3a2 2 0 0 1 2-2zm0 3v14h10V4zm5 15.5a1.2 1.2 0 1 0 0 2.4 1.2 1.2 0 0 0 0-2.4z"/></svg>742 318 6025</li>
      <li><svg viewBox="0 0 24 24"><path d="M6 3h12v5H6zM3 9h18a1 1 0 0 1 1 1v7h-4v4H6v-4H2v-7a1 1 0 0 1 1-1zm5 6v4h8v-4z"/></svg>527 463 8810</li>
      <li><svg viewBox="0 0 24 24"><path d="M2 5h20v14H2zm2 2v.5l8 5 8-5V7l-8 5z"/></svg>office@arvenhealth.com</li>
    </ul>

    <address class="address">
      2140 Harbor View Road<br>
      Fairbanks<br>
      Alaska 99701<br>
      <span class="website">www.arvenhealth.com</span>
    </address>
  </section>
</body>
</html>
```